Butcher shop

We have 2 butcher shops:

Shop 7, Ridgeway Court, Aberdeen NSW 2336
Ph 02 6519 4482

58 Partridge St, Scone NSW 2337
Ph 02 6538 2170

ABN 47 308 915 226

I would like this info on reverse of card and my personal info on front of card. I have a logo I would like to use also. Require a very smooth thick matte card, with colour both sides.

Front of card should say:

Lorna Tewsbury
Accounts

Ph 0427 615 903
E lornatewsbury@mailnest.example

Industry/Entity Type

Shop

Contact Information for Business Card

Lorna Tewsbury
Ph 0427 615 903

Logo Text

Tewsbury's Quality Meats

Logo styles of interest
Pictorial/Combination Logo
Requirements
Must have
• We use Century Gothic Font

```html
<!DOCTYPE html>
<html lang="en">
<head>
<meta charset="utf-8">
<title>Tewsbury's Quality Meats – Business Card</title>
<link rel="stylesheet" href="https://fonts.googleapis.com/css2?family=Questrial&display=swap">
<style>
  :root {
    --page: #e6e8ea;
    --slate-light: #7092a0;
    --slate-dark: #56737f;
    --ink: #141a1e;
    --sky: #8fd0e6;
    --sky-deep: #5bb6d6;
    --paper: #fbfbfb;
    --white: #ffffff;
    --edge: #2a2f33;
  }
  * { box-sizing: border-box; margin: 0; padding: 0; }
  html, body { width: 1200px; height: 983px; overflow: hidden; }
  body {
    background: var(--page);
    font-family: "Questrial", "Century Gothic", sans-serif;
    position: relative;
  }
  .card {
    position: absolute;
    left: 280px;
    width: 640px;
    height: 390px;
    border-radius: 4px;
    box-shadow: 0 8px 24px rgba(0,0,0,.18);
    overflow: hidden;
  }

  /* Reverse side */
  .card--back {
    top: 70px;
    background: linear-gradient(160deg, var(--slate-light), var(--slate-dark));
    color: var(--white);
  }
  .card__texture { position: absolute; inset: 0; }
  .brand--back {
    position: absolute;
    top: 78px; left: 0; right: 0;
    text-align: center;
    color: var(--ink);
    font-size: 40px;
    line-height: 1.05;
  }
  .brand__mark {
    display: block;
    width: 14px; height: 14px;
    margin: 0 auto 16px;
    background: var(--ink);
  }
  .abn {
    position: absolute;
    top: 222px; left: 0; right: 0;
    text-align: center;
    font-size: 19px;
    letter-spacing: .5px;
  }
  .shop {
    position: absolute;
    bottom: 34px;
    display: grid;
    grid-template-columns: auto auto;
    column-gap: 12px;
    row-gap: 4px;
    font-size: 16px;
  }
  .shop--aberdeen { left: 36px; }
  .shop--scone { right: 36px; }
  .shop__label { color: var(--sky); font-size: 17px; }
  .shop__value { color: var(--white); }
  .shop__address { grid-column: 1 / 3; font-size: 14px; margin-top: 2px; }

  /* Front side */
  .card--front {
    top: 520px;
    background: var(--paper);
    color: var(--ink);
  }
  .brand--front {
    position: absolute;
    top: 44px; left: 44px;
    font-size: 22px;
    line-height: 1.1;
    color: var(--ink);
  }
  .brand--front .brand__mark {
    width: 10px; height: 10px;
    margin: 0 0 10px 60px;
  }
  .edge-bar {
    position: absolute;
    left: 0; top: 190px;
    width: 6px; height: 52px;
    background: var(--edge);
  }
  .person {
    position: absolute;
    top: 196px; left: 44px;
    color: var(--sky-deep);
    font-size: 24px;
    line-height: 1.1;
  }
  .contact {
    position: absolute;
    top: 282px; left: 44px;
    display: grid;
    grid-template-columns: 62px auto;
    row-gap: 6px;
    font-size: 15px;
  }
  .contact__label { color: var(--sky-deep); font-size: 14px; }
</style>
</head>
<body>

<section class="card card--back" aria-label="Card reverse">
  <svg class="card__texture" width="640" height="390" role="img" aria-label="Soft diamond texture across the card">
    <defs>
      <linearGradient id="sheen" x1="0" y1="0" x2="1" y2="1">
        <stop offset="0" stop-color="#ffffff" stop-opacity=".10"/>
        <stop offset="1" stop-color="#000000" stop-opacity=".08"/>
      </linearGradient>
    </defs>
    <rect width="640" height="390" fill="url(#sheen)"/>
  </svg>

  <div class="brand brand--back">
    <span class="brand__mark"></span>
    Tewsbury's<br>Quality Meats
  </div>

  <p class="abn">ABN 47 308 915 226</p>

  <div class="shop shop--aberdeen">
    <span class="shop__label">Phone:</span><span class="shop__value">02 6519 4482</span>
    <span class="shop__label">Address:</span><span></span>
    <span class="shop__value shop__address">Shop 7, Ridgeway Court, Aberdeen NSW 2336</span>
  </div>

  <div class="shop shop--scone">
    <span class="shop__label">Phone:</span><span class="shop__value">02 6538 2170</span>
    <span class="shop__label">Address:</span><span></span>
    <span class="shop__value shop__address">58 Partridge St, Scone NSW 2337</span>
  </div>
</section>

<section class="card card--front" aria-label="Card front">
  <div class="brand brand--front">
    <span class="brand__mark"></span>
    Tewsbury's<br>Quality Meats
  </div>

  <span class="edge-bar"></span>

  <div class="person">
    <p class="person__name">Lorna Tewsbury</p>
    <p class="person__role">Accounts</p>
  </div>

  <div class="contact">
    <span class="contact__label">Phone:</span><span>0427 615 903</span>
    <span class="contact__label">Email:</span><span>lornatewsbury@mailnest.example</span>
  </div>
</section>

</body>
</html>
```